Creative Brief
Investment Banking Company Stationary
Business card, Letterhead, Envelope, Fax Cover
Professional
Daniyar Ospanturov
Managing Partner
27B Zheltoksan St,
Almaty, 050118
Kazakhstan
dospanturov@mailvero.kz
www.veltrafin.kz
The name of the company is Veltra Finance, LLP. In addition to the logo there should be text that includes the official name of the company.
I will need business cards for 3 other employees as well. Please message me for their relevant info.
Logo or blank

```html
<!DOCTYPE html>
<html lang="en">
<head>
<meta charset="utf-8">
<title>Veltra Finance Stationery</title>
<link href="https://fonts.googleapis.com/css2?family=Arimo:wght@400;700&display=swap" rel="stylesheet">
<style>
  :root {
    --backdrop: #676767;
    --navy: #2f4468;
    --paper: #ffffff;
    --ink: #2a2a2a;
    --muted: #555b66;
    --ghost: #dcdee3;
  }
  * { box-sizing: border-box; margin: 0; padding: 0; }
  html, body { width: 1200px; height: 685px; overflow: hidden; background: var(--backdrop); }
  body { font-family: "Arimo", Arial, sans-serif; color: var(--ink); }
  .canvas { position: relative; width: 1200px; height: 685px; overflow: hidden; background: var(--backdrop); }

  .brand { position: absolute; display: flex; align-items: center; gap: 6px; }
  .brand-square { display: block; flex: none; background: var(--navy); }
  .brand-name { font-family: "Arimo", Arial, sans-serif; font-weight: 700; color: var(--navy); white-space: nowrap; }

  /* Business card */
  .card { position: absolute; left: 12px; width: 204px; }
  .card-front { top: 137px; height: 144px; background: var(--navy); box-shadow: 0 2px 5px rgba(0,0,0,.35); }
  .card-front .brand { left: 0; right: 0; top: 58px; justify-content: center; }
  .card-front .brand-square { width: 12px; height: 12px; background: var(--paper); }
  .card-front .brand-name { color: var(--paper); font-size: 15px; }
  .card-front .tagline { position: absolute; left: 28px; right: 28px; top: 106px; text-align: center; font-size: 6px; color: var(--paper); border-top: 1px solid rgba(255,255,255,.5); padding-top: 4px; white-space: nowrap; }
  .card-back { top: 281px; height: 91px; background: var(--paper); box-shadow: 0 2px 5px rgba(0,0,0,.35); }
  .card-back .brand { left: 10px; top: 12px; gap: 4px; }
  .card-back .brand-square { width: 7px; height: 7px; }
  .card-back .brand-name { font-size: 9px; }
  .card-back .person { position: absolute; right: 10px; top: 9px; text-align: right; font-size: 6px; line-height: 1.4; color: var(--muted); }
  .card-back .address { position: absolute; left: 10px; top: 55px; font-size: 5.5px; line-height: 1.4; color: var(--muted); }
  .card-back .phones { position: absolute; right: 10px; top: 55px; text-align: right; font-size: 5.5px; line-height: 1.4; color: var(--muted); }

  /* Letterhead */
  .letterhead { position: absolute; left: 226px; top: 12px; width: 374px; height: 636px; background: var(--paper); box-shadow: 0 2px 6px rgba(0,0,0,.35); }
  .letterhead .brand { left: 38px; top: 54px; }
  .letterhead .brand-square { width: 12px; height: 12px; }
  .letterhead .brand-name { font-size: 15px; }
  .letterhead .contact { position: absolute; right: 24px; top: 34px; text-align: right; font-size: 7px; line-height: 1.5; color: var(--muted); }
  .ghost-mark { position: absolute; display: flex; align-items: center; justify-content: center; }
  .ghost-mark .brand-square { background: var(--ghost); }
  .ghost-mark .brand-name { color: var(--ghost); }
  .letterhead .ghost-mark { left: 0; right: 0; top: 386px; gap: 12px; }
  .letterhead .ghost-mark .brand-square { width: 30px; height: 30px; }
  .letterhead .ghost-mark .brand-name { font-size: 38px; }
  .letterhead .footer { position: absolute; left: 0; right: 0; top: 612px; text-align: center; font-size: 6.5px; line-height: 1.5; color: var(--muted); }

  /* Envelope */
  .envelope { position: absolute; left: 629px; top: 288px; width: 571px; height: 324px; }
  .envelope-flap { position: absolute; left: 0; top: 0; width: 571px; height: 76px; }
  .envelope-body { position: absolute; left: 0; top: 70px; width: 571px; height: 254px; background: var(--paper); box-shadow: 0 3px 6px rgba(0,0,0,.35); }
  .envelope .flap-brand { left: 0; width: 571px; top: 40px; justify-content: center; gap: 5px; }
  .envelope .flap-brand .brand-square { width: 9px; height: 9px; background: var(--paper); }
  .envelope .flap-brand .brand-name { color: var(--paper); font-size: 12px; }
  .envelope .body-brand { left: 12px; top: 98px; gap: 5px; }
  .envelope .body-brand .brand-square { width: 9px; height: 9px; }
  .envelope .body-brand .brand-name { font-size: 12px; }
  .envelope .ghost-mark { left: 300px; width: 250px; top: 222px; gap: 8px; }
  .envelope .ghost-mark .brand-square { width: 20px; height: 20px; }
  .envelope .ghost-mark .brand-name { font-size: 26px; }
  .envelope .address { position: absolute; left: 12px; top: 281px; font-size: 6.5px; line-height: 1.6; color: var(--muted); }
  .envelope .rule { position: absolute; left: 0; right: 0; top: 316px; height: 4px; background: var(--navy); }
</style>
</head>
<body>
<main class="canvas">

  <section class="card card-front">
    <div class="brand">
      <span class="brand-square"></span>
      <span class="brand-name">Veltra Finance</span>
    </div>
    <p class="tagline">Veltra Finance, LLP | www.veltrafin.kz</p>
  </section>

  <section class="card card-back">
    <div class="brand">
      <span class="brand-square"></span>
      <span class="brand-name">Veltra Finance</span>
    </div>
    <div class="person">Daniyar Ospanturov<br>Managing Partner</div>
    <div class="address">27B Zheltoksan St,<br>Almaty, 050118<br>Kazakhstan</div>
    <div class="phones">Ph: +7 (727) 300 1122<br>Fax: +7 (727) 300 1123<br>dospanturov@mailvero.kz</div>
  </section>

  <section class="letterhead">
    <div class="brand">
      <span class="brand-square"></span>
      <span class="brand-name">Veltra Finance</span>
    </div>
    <div class="contact">dospanturov@mailvero.kz<br>www.veltrafin.kz</div>
    <div class="ghost-mark">
      <span class="brand-square"></span>
      <span class="brand-name">Veltra Finance</span>
    </div>
    <div class="footer">27B Zheltoksan St, Almaty, 050118 Kazakhstan<br>Ph: +7 (727) 300 1122 Cell: +7 (701) 455 2310 Fax: +7 (727) 300 1123</div>
  </section>

  <section class="envelope">
    <svg class="envelope-flap" viewBox="0 0 571 76" aria-hidden="true">
      <path d="M0,76 L0,68 C110,68 180,4 262,4 C344,4 420,68 571,68 L571,76 Z" fill="var(--navy)"/>
    </svg>
    <div class="envelope-body"></div>
    <div class="brand flap-brand">
      <span class="brand-square"></span>
      <span class="brand-name">Veltra Finance</span>
    </div>
    <div class="brand body-brand">
      <span class="brand-square"></span>
      <span class="brand-name">Veltra Finance</span>
    </div>
    <div class="ghost-mark">
      <span class="brand-square"></span>
      <span class="brand-name">Veltra Finance</span>
    </div>
    <div class="address">27B Zheltoksan St, Almaty, 050118 Kazakhstan<br>Ph: +7 (727) 300 1122 Cell: +7 (701) 455 2310 Fax: +7 (727) 300 1123<br>Email: dospanturov@mailvero.kz &nbsp;&nbsp; Web: www.veltrafin.kz</div>
    <div class="rule"></div>
  </section>

</main>
</body>
</html>
```